Tidewalk Intro Course QM Dive Bonaire

QM Dive is looking for a great flyer to promote our Tidewalk Intro Course around Bonaire, the Caribbean.

Bonaire is shore dive capital of the world.
Our guests rent a pick-up truck. we would like to inform them about the possibilities of the Tidewalk Intro Dive.

We have the logo, images and text available. Its the catchy and mind blowing design we are looking for to create an eye-catch flyer.
One side will be in English, the other side will be in Dutch.

Target Market(s)

Visitors (non divers) of the island Bonaire

Industry/Entity Type

Diving industry

Font styles to use
Sans Serif

Colors
0094D4
00A9DD
6FCCEA
C7EBF8
E9F6FB
F0912C
F2A743
F7CA91
FBE8D2
FDF5EE

Requirements
Must have
• The picture with the car and divers next to it is mandatory. Inspire to go for a tidewalk intro dive, show the beauty under water, easy to come dive with us, just takes half a day
Should not have
• Should not have pictures taken not around Bonaire.

```html
<!DOCTYPE html>
<html lang="en">
<head>
<meta charset="utf-8">
<title>Tidewalk Intro Course – QM Dive Bonaire</title>
<link rel="stylesheet" href="https://fonts.googleapis.com/css2?family=Montserrat:wght@400;600;700;800;900&family=Open+Sans:wght@400;600;700&display=swap">
<style>
  :root{
    --blue-deep:#0a2a73;
    --blue-navy:#0d3a8f;
    --blue:#0094D4;
    --blue-bright:#00A9DD;
    --blue-soft:#6FCCEA;
    --blue-pale:#C7EBF8;
    --blue-mist:#E9F6FB;
    --orange:#F0912C;
    --orange-warm:#F2A743;
    --orange-soft:#F7CA91;
    --orange-pale:#FBE8D2;
    --cream:#FDF5EE;
    --white:#ffffff;
    --ink:#1c2a4a;
  }
  *{box-sizing:border-box;margin:0;padding:0}
  html,body{width:855px;height:1200px;overflow:hidden;background:#ffffff}
  body{font-family:"Open Sans",Arial,sans-serif;color:var(--ink)}
  .flyer{position:relative;width:855px;height:1200px;overflow:hidden;background:var(--white)}

  .hero-photo{position:absolute;left:0;top:0;width:855px;height:560px;
    background:radial-gradient(ellipse at 45% 25%,#2b6fc4 0%,#14489f 40%,var(--blue-deep) 80%)}
  .diver-photo{position:absolute;left:300px;top:0;width:250px;height:300px;
    background:radial-gradient(ellipse at 50% 40%,#3c88d4 0%,#1b56aa 60%,rgba(20,72,159,0) 100%)}

  .title-block{position:absolute;right:48px;top:52px;width:330px;text-align:center;color:var(--white);z-index:2}
  .title-kicker{font-family:"Montserrat",sans-serif;font-weight:800;font-size:30px;letter-spacing:2px}
  .title-main{font-family:"Montserrat",sans-serif;font-weight:900;font-size:56px;line-height:.95;
    color:var(--orange-warm);text-transform:uppercase;margin-top:4px}
  .title-place{font-family:"Montserrat",sans-serif;font-weight:700;font-size:18px;letter-spacing:2px;margin-top:8px}
  .title-place b{font-size:24px}
  .title-intro{font-size:13px;line-height:1.45;margin-top:16px;color:var(--blue-pale)}

  .reef-circle{position:absolute;left:55px;top:195px;width:145px;height:145px;border-radius:50%;z-index:2;
    border:4px solid var(--white);background:radial-gradient(circle at 40% 40%,var(--blue-soft),var(--blue) 55%,var(--blue-navy))}
  .hours{position:absolute;left:42px;top:350px;width:170px;text-align:center;z-index:2}
  .hours-label{font-family:"Montserrat",sans-serif;font-weight:700;font-size:17px;color:var(--orange-warm)}
  .hours-time{font-family:"Montserrat",sans-serif;font-weight:800;font-size:22px;color:var(--white);white-space:nowrap}

  .wave-band{position:absolute;left:0;top:440px;width:855px;height:380px;z-index:1}

  .paradise{position:absolute;left:36px;top:800px;width:380px;z-index:2}
  .paradise h2{font-family:"Montserrat",sans-serif;font-weight:800;font-size:27px;color:var(--blue-navy)}
  .paradise h2 span{color:var(--blue)}
  .paradise-box{margin-top:12px;background:var(--blue);color:var(--white);padding:16px 18px;font-size:12.5px;line-height:1.5;border-radius:4px}
  .paradise-call{margin-top:16px;font-family:"Montserrat",sans-serif;font-weight:700;font-size:13px;line-height:1.45;color:var(--orange);text-transform:uppercase}

  .passion-panel{position:absolute;left:440px;top:715px;width:415px;height:345px;z-index:2}
  .passion{position:absolute;left:465px;top:742px;width:370px;color:var(--white);z-index:3}
  .passion h2{font-family:"Montserrat",sans-serif;font-weight:800;font-size:24px;line-height:1.15;text-align:center}
  .passion h2 span{color:var(--orange-warm)}
  .passion ul{list-style:none;margin-top:14px}
  .passion li{position:relative;padding-left:18px;font-size:12px;line-height:1.35;margin-bottom:5px}
  .passion li::before{content:"";position:absolute;left:2px;top:5px;width:7px;height:7px;border-radius:50%;background:var(--orange-warm)}

  .footer{position:absolute;left:0;top:1060px;width:855px;height:140px;background:var(--orange);z-index:4}
  .brand{position:absolute;left:36px;top:40px;display:flex;align-items:center;gap:10px}
  .brand-mark{width:42px;height:42px;border-radius:50%;background:var(--blue-navy)}
  .brand-name{font-family:"Montserrat",sans-serif;font-weight:800;font-size:24px;color:var(--blue-navy)}
  .booking{position:absolute;left:250px;top:30px;text-align:center;color:var(--white)}
  .booking-label{font-family:"Montserrat",sans-serif;font-weight:800;font-size:18px;letter-spacing:1px}
  .booking-phone{font-family:"Montserrat",sans-serif;font-weight:800;font-size:36px;margin-top:2px}
  .contacts{position:absolute;left:560px;top:32px;color:var(--white);font-weight:700;font-size:15px;line-height:1.7;
    padding-left:18px;border-left:2px solid var(--orange-pale)}
</style>
</head>
<body>
<main class="flyer">
  <div class="hero-photo" role="img" aria-label="Underwater scene off Bonaire with deep blue water"></div>
  <div class="diver-photo" role="img" aria-label="Scuba diver swimming above the reef"></div>

  <header class="title-block">
    <p class="title-kicker">TIDEWALK</p>
    <h1 class="title-main">Intro Course</h1>
    <p class="title-place">ON <b>BONAIRE</b></p>
    <p class="title-intro">Explore a whole new underwater paradise. Under the guidance of a dive instructor you will discover Bonaire's reefs in a fun and easy way.</p>
  </header>

  <div class="reef-circle" role="img" aria-label="Divers exploring the coral reef"></div>
  <div class="hours">
    <p class="hours-label">Opening hours</p>
    <p class="hours-time">8:00AM - 5:00PM</p>
  </div>

  <svg class="wave-band" viewBox="0 0 855 380">
    <defs>
      <linearGradient id="truckTones" x1="0" y1="0" x2="0" y2="1">
        <stop offset="0" stop-color="#7cc7ec"/>
        <stop offset=".55" stop-color="#cfd8df"/>
        <stop offset="1" stop-color="#d9c8a8"/>
      </linearGradient>
    </defs>
    <path d="M0 30 C200 -10 420 60 855 10 L855 330 C620 380 300 300 0 350 Z" fill="#ffffff"/>
    <path d="M0 50 C220 10 430 80 855 30 L855 300 C620 350 300 280 0 320 Z" fill="url(#truckTones)" role="img" aria-label="Two divers in gear standing next to the QM Dive pick-up truck on the shore"/>
    <path d="M0 320 C300 280 620 350 855 300 L855 330 C620 380 300 310 0 352 Z" fill="var(--blue-bright)"/>
    <path d="M0 352 C300 310 620 380 855 330 L855 380 L0 380 Z" fill="#ffffff"/>
  </svg>

  <section class="paradise">
    <h2>Underwater <span>PARADISE</span></h2>
    <p class="paradise-box">Bonaire is the place to learn how to scuba dive. After a brief introduction we will directly dive into the sea where the reef starts in shallow waters. We lower the pace, you will get to know the reef and its colorful fish and corals.</p>
    <p class="paradise-call">Stop by at our front office and we are happy to answer all your questions or to book your Tidewalk Intro Dive!</p>
  </section>

  <svg class="passion-panel" viewBox="0 0 415 345" aria-hidden="true">
    <path d="M0 40 C120 0 280 10 415 0 L415 345 L0 345 Z" fill="var(--blue)"/>
  </svg>
  <section class="passion">
    <h2>Develop <span>A PASSION</span><br>for <span>MARINE LIFE</span></h2>
    <ul>
      <li>Ages 10 and up can sign up for an intro dive</li>
      <li>You'll dive straight from the shore after a brief theory introduction</li>
      <li>The Tidewalk Intro Dive is done in just 3-4 hours</li>
      <li>Before participating you are required to fill out a medical questionnaire</li>
      <li>A group consists of a maximum of 4 people</li>
      <li>Experience the splendor of the ocean without much distraction by other divers</li>
      <li>And enjoy a lot of personal attention given by your instructor</li>
    </ul>
  </section>

  <footer class="footer">
    <div class="brand">
      <span class="brand-mark"></span>
      <span class="brand-name">Reefline</span>
    </div>
    <div class="booking">
      <p class="booking-label">BOOK NOW</p>
      <p class="booking-phone">(+599) 555 01 23</p>
    </div>
    <div class="contacts">
      <p>qmdive-bonaire.com</p>
      <p>info@qmdive-bonaire.com</p>
      <p>Kaya Coral 12, Kralendijk, Bonaire</p>
    </div>
  </footer>
</main>
</body>
</html>
```